Security and Automation Company based in Texas and needs logo design also

Looking for a new logo design for our company - we are based in Texas and specialize in camera, security and home automation - We do want the main company name(Brightline Guard and Controls of Texas) with our parent company in small letters below (a Veloran Partners, LLC Company) and our License number needs to be included in the design - K74836 - Darker shades of blue preferred

Target Market(s)

We work with everyone from home to large corporate - so clean design would be helpful

Industry/Entity Type

It Company

Contact Information for Business Card

PO Box 4719
Cedar Hollow, Texas 75961
Leave a spot for the phone number and email address

Logo Text

Brightline Guard and Controls of Texas/a Veloran Partners Company/K74836

Font styles to use
Sans Serif

Colors
0255a3

```html
<!DOCTYPE html>
<html lang="en">
<head>
<meta charset="utf-8">
<title>Brightline Guard and Controls of Texas — Business Card</title>
<link rel="stylesheet" href="https://fonts.googleapis.com/css2?family=Bebas+Neue&family=Lato:wght@400&display=swap">
<style>
  :root {
    --brand-blue: #0255a3;
    --ink-dark: #262626;
    --ink-row: #2b2b2b;
    --row-line: #3f3f3f;
    --paper: #ffffff;
    --backdrop: #e4dccf;
    --muted-grey: #4d4d4d;
    --frame-line: rgba(255,255,255,0.35);
  }
  * { box-sizing: border-box; margin: 0; padding: 0; }
  html, body { width: 1200px; height: 1200px; overflow: hidden; }
  body { background: var(--backdrop); position: relative; font-family: "Lato", sans-serif; }

  .card {
    position: absolute; top: 135px; width: 513px; height: 854px;
    box-shadow: 0 6px 18px rgba(0,0,0,0.25);
    overflow: hidden;
  }
  .card--front { left: 54px; background: var(--paper); }
  .card--back { left: 642px; background: var(--brand-blue); }

  /* brand lockup */
  .brand { position: absolute; display: flex; align-items: center; }
  .brand__mark { width: 82px; height: 82px; border-radius: 50%; border: 9px solid var(--brand-blue); flex: none; }
  .brand__divider { width: 1px; height: 100px; background: var(--brand-blue); opacity: 0.6; margin: 0 24px 0 26px; flex: none; }
  .brand__text { text-align: center; }
  .brand__name {
    font-family: "Bebas Neue", sans-serif; font-size: 35px; line-height: 34px;
    color: var(--brand-blue); letter-spacing: 0.2px;
  }
  .brand__parent { font-size: 16px; color: var(--muted-grey); margin-top: 4px; white-space: nowrap; }
  .brand__license {
    display: flex; align-items: center; justify-content: center; gap: 6px;
    font-size: 15px; color: var(--muted-grey); margin-top: 2px;
  }
  .brand__rule { height: 3px; width: 78px; background: var(--brand-blue); border-radius: 2px; }
  .card--front .brand { left: 60px; top: 118px; }

  .card--back .brand { left: 78px; top: 328px; }
  .card--back .brand__mark { border-color: var(--paper); }
  .card--back .brand__divider { background: var(--paper); opacity: 0.5; }
  .card--back .brand__name { color: var(--paper); }
  .card--back .brand__parent, .card--back .brand__license { color: var(--paper); }
  .card--back .brand__rule { background: var(--paper); }

  .back__frame { position: absolute; inset: 29px 29px 29px 29px; border: 1px solid var(--frame-line); }

  /* contact panel */
  .contact {
    position: absolute; left: 0; right: 0; top: 384px; bottom: 0;
    background: var(--ink-dark); border-top: 5px solid var(--brand-blue);
  }
  .contact__row {
    height: 107px; display: flex; align-items: center;
    border-bottom: 2px solid var(--row-line); background: var(--ink-row);
    padding-left: 63px;
  }
  .contact__row:last-child { border-bottom: 0; height: 140px; align-items: flex-start; padding-top: 12px; }
  .contact__icon {
    width: 70px; height: 70px; border-radius: 50%; border: 3px solid var(--brand-blue);
    display: flex; align-items: center; justify-content: center; flex: none;
  }
  .contact__icon svg { width: 30px; height: 30px; fill: #fff; }
  .contact__text { margin-left: 26px; color: #fff; font-size: 24px; line-height: 29px; }
  .contact__name { font-size: 30px; line-height: 32px; }
  .contact__role { font-size: 20px; color: #d5d5d5; line-height: 22px; }
</style>
</head>
<body>

<section class="card card--front">
  <div class="brand">
    <div class="brand__mark"></div>
    <div class="brand__divider"></div>
    <div class="brand__text">
      <div class="brand__name">Brightline Guard and<br>Controls of Texas</div>
      <div class="brand__parent">a Veloran Partners, LLC Company</div>
      <div class="brand__license"><span class="brand__rule"></span>K74836<span class="brand__rule"></span></div>
    </div>
  </div>

  <div class="contact">
    <div class="contact__row">
      <div class="contact__icon"><svg viewBox="0 0 24 24"><circle cx="12" cy="8" r="5"/><path d="M2 23c0-6 4.5-9 10-9s10 3 10 9z"/></svg></div>
      <div class="contact__text"><div class="contact__name">JOHN DOE</div><div class="contact__role">CEO</div></div>
    </div>
    <div class="contact__row">
      <div class="contact__icon"><svg viewBox="0 0 24 24"><path d="M6.6 10.8a15 15 0 0 0 6.6 6.6l2.2-2.2a1 1 0 0 1 1-.25 11.4 11.4 0 0 0 3.6.6 1 1 0 0 1 1 1V20a1 1 0 0 1-1 1A17 17 0 0 1 3 4a1 1 0 0 1 1-1h3.5a1 1 0 0 1 1 1c0 1.25.2 2.45.6 3.6a1 1 0 0 1-.25 1z"/></svg></div>
      <div class="contact__text">+1 123 423 1010<br>+1 123 423 1010</div>
    </div>
    <div class="contact__row">
      <div class="contact__icon"><svg viewBox="0 0 24 24" fill="none" stroke="#fff" stroke-width="1.8"><circle cx="12" cy="12" r="10"/><ellipse cx="12" cy="12" rx="4.5" ry="10"/><path d="M2 12h20M4 6.5h16M4 17.5h16M12 2v20"/></svg></div>
      <div class="contact__text">mail@yourwebsite.com<br>www.yourwebsite.com</div>
    </div>
    <div class="contact__row">
      <div class="contact__icon"><svg viewBox="0 0 24 24"><path d="M12 3 1 12.5h3V21h6v-6h4v6h6v-8.5h3z"/></svg></div>
      <div class="contact__text">PO Box 4719<br>Cedar Hollow,<br>Texas 75961</div>
    </div>
  </div>
</section>

<section class="card card--back">
  <div class="back__frame"></div>
  <div class="brand">
    <div class="brand__mark"></div>
    <div class="brand__divider"></div>
    <div class="brand__text">
      <div class="brand__name">Brightline Guard and<br>Controls of Texas</div>
      <div class="brand__parent">a Veloran Partners, LLC Company</div>
      <div class="brand__license"><span class="brand__rule"></span>K74836<span class="brand__rule"></span></div>
    </div>
  </div>
</section>

</body>
</html>
```